New Custom Pizza Box Design Project For Independant Restaurant

We are looking for creative designs for our new custom printed pizza boxes. Designs should include the following:

-Our logo & company name
-A color scheme similar to our current logo
-Our physical and URL addresses & phone number (menu is attached)
-Ability to scale the design across several box sizes (10x10x2, 14x14x2, 18x13x2,
26x18x2)
- Any creative flair you think will make for the best design

Design can be on a white or kraft (tan) box.
Designs can be either two or three ink colors.

***Please note, designs must be able to be screen printed on boxes***
Updates

Reason: Still debating which to choose

Target Market(s)

Industry/Entity Type

Pizza Delivery

Font styles to use
Other font styles liked:
• Please use font similar to our logo text

Requirements
Must have
• -2 or 3 ink colors
• -company name, address, phone number, URL
• -company logo and colors
• -flexibility to use on different box sizes (10x10x2, 14x14x2, 18x13x2,
• 26x18x2)
• -utilize full printable area on boxes (including 2" dimension on box sides)
• ***Please note, designs must be able to be screen printed on boxes***
Should not have
• Design features with strong similarities to existing designs of other pizzerias

```html
<!DOCTYPE html>
<html lang="en">
<head>
<meta charset="utf-8">
<title>Marco's Hentown Pizzeria – Box Lid</title>
<link rel="stylesheet" href="https://fonts.googleapis.com/css2?family=Oswald:wght@400&display=swap">
<style>
  :root {
    --lid-yellow: #f2b81f;
    --lid-yellow-light: #f6c947;
    --sketch-brown: #c98f1c;
    --sketch-shadow: #b5801c;
    --ink-charcoal: #3b3a38;
  }
  html, body {
    margin: 0;
    padding: 0;
    width: 1200px;
    height: 1200px;
    overflow: hidden;
    background: var(--lid-yellow);
  }
  .box-lid {
    display: block;
    width: 1200px;
    height: 1200px;
  }
  .lid-text {
    font-family: "Oswald", "Arial Narrow", sans-serif;
    font-weight: 400;
    fill: var(--ink-charcoal);
  }
  .sketch { fill: var(--sketch-brown); opacity: 0.45; }
  .sketch-deep { fill: var(--sketch-shadow); opacity: 0.4; }
  .brand-dot { fill: var(--ink-charcoal); }
</style>
</head>
<body>
<svg class="box-lid" viewBox="0 0 1200 1200" xmlns="http://www.w3.org/2000/svg">
  <defs>
    <radialGradient id="lid-glow" cx="50%" cy="50%" r="70%">
      <stop offset="0%" stop-color="var(--lid-yellow)"/>
      <stop offset="100%" stop-color="var(--lid-yellow-light)"/>
    </radialGradient>
  </defs>

  <rect class="lid-background" width="1200" height="1200" fill="url(#lid-glow)"/>

  <!-- ingredient sketches -->
  <g class="ingredient-sketches">
    <ellipse class="sketch" cx="330" cy="210" rx="200" ry="120" role="img" aria-label="Sketched mushrooms and herbs"/>
    <path class="sketch" d="M790 260 L1090 120 L1130 210 Z" role="img" aria-label="Sketched pizza slice"/>
    <ellipse class="sketch-deep" cx="230" cy="500" rx="180" ry="60" transform="rotate(-18 230 500)" role="img" aria-label="Sketched chili peppers"/>
    <ellipse class="sketch" cx="1010" cy="460" rx="120" ry="90" role="img" aria-label="Sketched mushrooms"/>
    <path class="sketch" d="M80 1000 L170 700 L380 900 L330 1010 Z" role="img" aria-label="Sketched wedge of cheese"/>
    <ellipse class="sketch" cx="1000" cy="940" rx="230" ry="120" role="img" aria-label="Sketched onions and vegetables"/>
  </g>

  <!-- header -->
  <text class="lid-text" x="600" y="105" font-size="100" text-anchor="middle" textLength="980" lengthAdjust="spacingAndGlyphs">WE DELIVER! 555-0142</text>

  <!-- brand name -->
  <g class="brand-name">
    <text class="lid-text" x="600" y="410" font-size="90" text-anchor="middle" letter-spacing="8">MARCO'S</text>
    <text class="lid-text" x="600" y="610" font-size="190" text-anchor="middle" textLength="760" lengthAdjust="spacingAndGlyphs">HENTOWN</text>
    <text class="lid-text" x="600" y="760" font-size="110" text-anchor="middle" letter-spacing="10">PIZZERIA</text>
    <circle class="brand-dot" cx="600" cy="830" r="20"/>
  </g>

  <!-- contact footer -->
  <text class="lid-text" x="600" y="1080" font-size="84" text-anchor="middle" textLength="780" lengthAdjust="spacingAndGlyphs">MARCOSHENTOWN.COM</text>
  <text class="lid-text" x="600" y="1168" font-size="62" text-anchor="middle" textLength="1070" lengthAdjust="spacingAndGlyphs">1275 LINDEN AVENUE, EASTBROOK PLAZA</text>
</svg>
</body>
</html>
```